Brochure required for international Sports event

We need an 8 page brochure designed for an international sports event to be hosted in Japan. We are a Travel Company providing packages for participants looking to travel to the event.
The brochure will feature information on the event as well as services our company can provide.
The Brochure is to be an 8 page A4 document in portrait layout.
The brochure needs to be provided both as a print ready document and digital brochure for emailing.
Brochure structure, copy, logo and imagery has been provided
As well as a example brochure design that we like for inspiration.
Link to icons - https://www.filorabox.com/sh/qk3ramvi8ptyzel/BBBqwLpRt7VmK3H9nX2cT8gRb?dl=0
Target Market(s)
Masters/Veterans Sports Participants
Industry/Entity Type
Travel
Colors
Designer to choose colors to be used in the design.
Look and feel

```html
<!DOCTYPE html>
<html lang="en">
<head>
<meta charset="utf-8">
<title>Hanami Travel – 2021 Games Brochure</title>
<link rel="stylesheet" href="https://fonts.googleapis.com/css2?family=Exo+2:ital,wght@0,400;0,500;0,600;0,700;0,800;1,400;1,500&display=swap">
<style>
:root{
  --backdrop:#3b3b3d;
  --paper:#eef0f5;
  --red:#d3182a;
  --deep-red:#7e1418;
  --ink:#1e1e22;
  --body:#4a4a52;
  --label:#6a6a72;
  --strip:#e2e3e8;
  --ghost:#b5c0d8;
  --white:#ffffff;
}
*{box-sizing:border-box;margin:0;padding:0}
html,body{width:1200px;height:2444px;overflow:hidden}
body{background:var(--backdrop);font-family:"Exo 2",sans-serif;position:relative}
.spread{position:absolute;left:65px;width:1070px;height:756px;overflow:hidden;background:var(--paper)}
.spread-cover{top:65px}
.spread-event{top:843px}
.spread-travel{top:1623px}
.page{position:absolute;top:0;width:535px;height:756px;overflow:hidden}
.page-left{left:0}
.page-right{left:535px}
.photo{position:absolute}
.deco{position:absolute;pointer-events:none}

/* cover back */
.temple-photo{inset:0;background:linear-gradient(180deg,#dfe8f3 0%,#c9d6e8 30%,#c23a2a 45%,#a8281d 58%,#8a8f97 72%,#b9bcc2 100%)}
.ghost-title{position:absolute;left:88px;top:88px;display:flex;align-items:flex-start;gap:14px;color:var(--ghost)}
.ghost-year{font-size:92px;font-weight:800;line-height:.9;letter-spacing:-2px}
.ghost-name{font-size:23px;font-weight:600;line-height:1.08;padding-top:6px}
.ghost-place{position:absolute;left:88px;top:182px;font-size:28px;font-weight:700;color:var(--ghost);display:flex;align-items:center;gap:10px}
.ghost-lines{width:130px;height:14px;background:repeating-linear-gradient(180deg,var(--ghost) 0 2px,transparent 2px 4px)}
.contact{position:absolute;left:0;width:535px;top:656px;text-align:center;color:var(--white);font-size:17px;font-weight:500;line-height:1.3;text-shadow:0 1px 3px rgba(0,0,0,.5)}

/* cover front */
.torii-photo{inset:0;background:linear-gradient(160deg,#9b1d1b 0%,#7a1312 40%,#5a0d0e 70%,#3c0a0b 100%)}
.cover-year{position:absolute;left:50px;top:72px;font-size:150px;font-weight:800;color:var(--white);line-height:1;letter-spacing:-3px}
.cover-name{position:absolute;left:52px;top:218px;color:var(--white);font-size:28px;font-weight:700;line-height:1.2}
.cover-name .lines{display:inline-block;width:58px;height:16px;margin-left:6px;vertical-align:middle;background:repeating-linear-gradient(180deg,var(--white) 0 2px,transparent 2px 4px)}
.date-band{position:absolute;left:0;top:314px;width:345px;height:37px;background:var(--white);color:var(--red);font-size:26px;font-weight:700;line-height:37px;padding-left:52px}
.brand{position:absolute;left:140px;top:568px;width:300px;text-align:center;color:var(--white)}
.brand-main{font-size:72px;font-weight:800;line-height:1;letter-spacing:1px}
.brand-sub{font-size:40px;font-weight:800;line-height:1;margin-top:2px;letter-spacing:1px}

/* headings & copy */
.heading{position:absolute;color:var(--red);font-size:26px;font-weight:700;letter-spacing:.2px}
.copy{position:absolute;color:var(--body);font-size:10.6px;line-height:1.45}
.copy p+p{margin-top:12px}

.runner-photo{left:0;top:395px;width:535px;height:361px;background:linear-gradient(120deg,#cfe0c2 0%,#e9d9c8 30%,#e6e24a 55%,#7a8b6a 80%,#506048 100%)}

/* sports */
.ball-photo{left:379px;top:0;width:156px;height:147px;background:radial-gradient(circle at 65% 60%,#c8642a 0,#9a4418 38%,#6d707a 40%,#a9acb4 100%)}
.sport-strip{position:absolute;left:0;width:535px;height:18px;background:var(--strip)}
.sport{position:absolute;width:120px;text-align:center}
.sport svg{display:block;margin:0 auto 4px;width:34px;height:34px;fill:var(--ink)}
.sport span{font-size:11.5px;font-style:italic;color:var(--label);white-space:nowrap}

/* venues */
.venue-map{left:42px;top:93px;width:459px;height:621px;background:linear-gradient(135deg,#2a3f7c 0%,#41a8d8 22%,#7b4ba6 40%,#7c6b2e 55%,#48ad4a 70%,#e8418d 88%,#f08030 100%)}

/* packages */
.sub{position:absolute;left:43px;top:208px;font-size:17px;color:var(--ink)}
.perk{position:absolute;display:flex;align-items:center;gap:14px;font-size:15.5px;font-weight:500;color:var(--ink);line-height:1.05}
.perk svg{width:26px;height:26px;fill:var(--ink);flex:none}
.luggage-photo{left:0;top:479px;width:535px;height:277px;background:linear-gradient(180deg,#e6e6ea 0%,#b82a34 30%,#6a6f7a 55%,#2a2c33 80%,#1f3d8a 100%)}
</style>
</head>
<body>

<svg width="0" height="0" style="position:absolute" aria-hidden="true">
  <symbol id="trophy" viewBox="0 0 34 34"><path d="M8 3h18v3h5v4c0 5-3 8-7 8.5-1 2.5-3 4-5 4.5V27h5v4H10v-4h5v-4c-2-.5-4-2-5-4.5C6 18 3 15 3 10V6h5zM6 9v1c0 3 1.5 5 3 5.5C8.5 14 8 12 8 9zm22 0h-2c0 3-.5 5-1 6.5 1.5-.5 3-2.5 3-5.5z"/></symbol>
</svg>

<!-- Spread 1: cover -->
<section class="spread spread-cover">
  <div class="page page-left">
    <div class="photo temple-photo" role="img" aria-label="Photo of a red shrine gate building with stone steps under a pale sky"></div>
    <div class="ghost-title"><div class="ghost-year">2021</div><div class="ghost-name">GLOBAL<br>VETERANS<br>GAMES</div></div>
    <div class="ghost-place">KANSAI, JAPAN <span class="ghost-lines"></span></div>
    <div class="contact">www.hanamigames2021.com<br>hello@hanamigames2021.com<br>PH: +61 2 9000 4812</div>
  </div>
  <div class="page page-right">
    <div class="photo torii-photo" role="img" aria-label="Photo of a tunnel of red shrine gates along a stone path"></div>
    <div class="cover-year">2021</div>
    <div class="cover-name">GLOBAL VETERANS GAMES<br>KANSAI, JAPAN<span class="lines"></span></div>
    <div class="date-band">14t to 30th MAY 2021</div>
    <div class="brand"><div class="brand-main">HANAMI</div><div class="brand-sub">TRAVEL</div></div>
  </div>
</section>

<!-- Spread 2: event and sports -->
<section class="spread spread-event">
  <div class="page page-left">
    <div class="heading" style="left:45px;top:40px">THE GLOBAL VETERANS GAMES</div>
    <div class="copy" style="left:45px;top:97px;width:450px">
      <p>The 2021 Global Veterans Games will be the 10th Edition of the Games and the first time it will be held in Asia. Since its inception in Toronto in 1985 the Global Veterans Games has grown to become the world's largest mass-participated international sports event.</p>
      <p>The 2021 Games will be held in the Kansai region in the west of Japan and will take place over 17 days from May 14 – 30. An estimated 50,000 participants will meet to play a total of 65 sports and explore this beautiful and alluring country.</p>
    </div>
    <div class="heading" style="left:45px;top:208px">KANSAI</div>
    <div class="copy" style="left:45px;top:280px;width:450px">
      <p>Kansai consists of seven prefectures and was formerly the political and cultural center of Japan for many centuries and includes the cities of Kyoto, Osaka, Nara and Kobe.</p>
      <p>The Kansai region is located in the center of the Japanese islands and is home to over 20 million people. The region is also host to a number of incredible sights including Osaka Castle, Fushimi Inari Shrine, Kinkaku-ji (the Golden Pavilion), Nara Deer Park, Dotonbori District Nishiki Markets and Arashiyama Bamboo Grove.</p>
    </div>
    <div class="photo runner-photo" role="img" aria-label="Photo of a veteran runner in a yellow singlet stretching his leg on a rail"></div>
    <svg class="deco" style="left:0;top:395px" width="535" height="361" aria-hidden="true">
      <polygon points="300,260 370,100 420,100 350,260" fill="#f2c230" opacity=".7"/>
      <polygon points="360,260 470,20 535,20 535,60 430,260" fill="var(--red)" opacity=".85"/>
      <polygon points="440,8 460,8 430,50 410,50" fill="#555"/>
      <polygon points="470,8 490,8 460,50 440,50" fill="#888"/>
      <polygon points="40,150 70,80 95,80 65,150" fill="var(--red)" opacity=".25"/>
    </svg>
  </div>
  <div class="page page-right">
    <svg class="deco" style="left:0;top:0" width="535" height="160" aria-hidden="true">
      <polygon points="200,145 290,0 390,0 300,145" fill="var(--red)"/>
      <polygon points="260,145 340,20 380,20 300,145" fill="var(--deep-red)" opacity=".6"/>
    </svg>
    <div class="photo ball-photo" role="img" aria-label="Photo of a basketball on a court floor"></div>
    <div class="heading" style="left:36px;top:40px">SPORTS</div>
    <div class="copy" style="left:36px;top:86px;width:180px">The 2021 Global Veterans Games will feature a total of 65 sports played in first class venues across the region. The 2021 Sports include:</div>

    <div class="sport-strip" style="top:211px"></div>
    <div class="sport-strip" style="top:274px"></div>
    <div class="sport-strip" style="top:337px"></div>
    <div class="sport-strip" style="top:400px"></div>
    <div class="sport-strip" style="top:463px"></div>
    <div class="sport-strip" style="top:526px"></div>
    <div class="sport-strip" style="top:589px"></div>
    <div class="sport-strip" style="top:652px"></div>
    <div class="sport-strip" style="top:715px"></div>

    <div class="sport" style="left:32px;top:172px"><svg><use href="#trophy"/></svg><span>Archery</span></div>
    <div class="sport" style="left:153px;top:172px"><svg><use href="#trophy"/></svg><span>Football</span></div>
    <div class="sport" style="left:271px;top:172px"><svg><use href="#trophy"/></svg><span>Orienteering</span></div>
    <div class="sport" style="left:381px;top:172px"><svg><use href="#trophy"/></svg><span>Water Polo</span></div>

    <div class="sport" style="left:32px;top:235px"><svg><use href="#trophy"/></svg><span>Athletics</span></div>
    <div class="sport" style="left:153px;top:235px"><svg><use href="#trophy"/></svg><span>Flying Disc<small>(Ultimate)</small></span></div>
    <div class="sport" style="left:271px;top:235px"><svg><use href="#trophy"/></svg><span>Rowing</span></div>
    <div class="sport" style="left:381px;top:235px"><svg><use href="#trophy"/></svg><span>Table Tennis</span></div>

    <div class="sport" style="left:32px;top:298px"><svg><use href="#trophy"/></svg><span>Badminton</span></div>
    <div class="sport" style="left:153px;top:298px"><svg><use href="#trophy"/></svg><span>Gateball</span></div>
    <div class="sport" style="left:271px;top:298px"><svg><use href="#trophy"/></svg><span>Rugby</span></div>
    <div class="sport" style="left:381px;top:298px"><svg><use href="#trophy"/></svg><span>Taekwondo</span></div>

    <div class="sport" style="left:32px;top:361px"><svg><use href="#trophy"/></svg><span>Baseball</span></div>
    <div class="sport" style="left:153px;top:361px"><svg><use href="#trophy"/></svg><span>Golf</span></div>
    <div class="sport" style="left:271px;top:361px"><svg><use href="#trophy"/></svg><span>Sailing</span></div>
    <div class="sport" style="left:381px;top:361px"><svg><use href="#trophy"/></svg><span>Tennis</span></div>

    <div class="sport" style="left:32px;top:424px"><svg><use href="#trophy"/></svg><span>Basketball</span></div>
    <div class="sport" style="left:153px;top:424px"><svg><use href="#trophy"/></svg><span>Handball</span></div>
    <div class="sport" style="left:271px;top:424px"><svg><use href="#trophy"/></svg><span>Shooting</span></div>
    <div class="sport" style="left:381px;top:424px"><svg><use href="#trophy"/></svg><span>Tenpin Bowling</span></div>

    <div class="sport" style="left:32px;top:487px"><svg><use href="#trophy"/></svg><span>Canoe</span></div>
    <div class="sport" style="left:153px;top:487px"><svg><use href="#trophy"/></svg><span>Hockey</span></div>
    <div class="sport" style="left:271px;top:487px"><svg><use href="#trophy"/></svg><span>Softball</span></div>
    <div class="sport" style="left:381px;top:487px"><svg><use href="#trophy"/></svg><span>Triathlon</span></div>

    <div class="sport" style="left:32px;top:550px"><svg><use href="#trophy"/></svg><span>Cycling</span></div>
    <div class="sport" style="left:153px;top:550px"><svg><use href="#trophy"/></svg><span>Judo</span></div>
    <div class="sport" style="left:271px;top:550px"><svg><use href="#trophy"/></svg><span>Soft Tennis</span></div>
    <div class="sport" style="left:381px;top:550px"><svg><use href="#trophy"/></svg><span>Tug of War</span></div>

    <div class="sport" style="left:32px;top:613px"><svg><use href="#trophy"/></svg><span>Dance Sports</span></div>
    <div class="sport" style="left:153px;top:613px"><svg><use href="#trophy"/></svg><span>Karate</span></div>
    <div class="sport" style="left:271px;top:613px"><svg><use href="#trophy"/></svg><span>Squash</span></div>
    <div class="sport" style="left:381px;top:613px"><svg><use href="#trophy"/></svg><span>Volleyball</span></div>

    <div class="sport" style="left:32px;top:676px"><svg><use href="#trophy"/></svg><span>Dragonboat</span></div>
    <div class="sport" style="left:153px;top:676px"><svg><use href="#trophy"/></svg><span>Lifesaving</span></div>
    <div class="sport" style="left:271px;top:676px"><svg><use href="#trophy"/></svg><span>Swimming</span></div>
    <div class="sport" style="left:381px;top:676px"><svg><use href="#trophy"/></svg><span>Weightlifting</span></div>
  </div>
</section>

<!-- Spread 3: venues and packages -->
<section class="spread spread-travel">
  <div class="page page-left">
    <svg class="deco" style="left:0;top:0" width="535" height="756" aria-hidden="true">
      <polygon points="20,400 90,260 120,260 50,400" fill="var(--red)" opacity=".12"/>
    </svg>
    <div class="heading" style="left:45px;top:40px">VENUES</div>
    <div class="photo venue-map" role="img" aria-label="Colour-coded venue map of the Kansai prefectures showing 59 disciplines of 35 sports"></div>
  </div>
  <div class="page page-right">
    <div class="heading" style="left:43px;top:40px">TOUR PACKAGES</div>
    <div class="copy" style="left:43px;top:111px;width:430px">Working with Airline and local Accommodation, Travel and Tour partners we have crafted Tour Packageswith quality hotels conveniently located to the various sports venues as well as transport links. As no trip to Japan is complete without a visit to Tokyo we have included Japan's capital and some of the major sights in the package.</div>
    <div class="sub">Package Include:</div>

    <div class="perk" style="left:43px;top:246px"><svg viewBox="0 0 26 26"><path d="M2 14l8-1 6-9h3l-3 9 6-1 2-3h2l-1 5 1 5h-2l-2-3-6-1 3 9h-3l-6-9-8-1z"/></svg>FLIGHTS</div>
    <div class="perk" style="left:43px;top:280px"><svg viewBox="0 0 26 26"><path d="M2 6h3v7h18v-3c0-1-1-2-2-2h-9v5H5V6zm0 10h22v5h-2v-2H4v2H2z"/></svg>ACCOMMODATION</div>
    <div class="perk" style="left:43px;top:314px"><svg viewBox="0 0 26 26"><path d="M13 2a11 11 0 110 22 11 11 0 010-22zm0 2a9 9 0 100 18 9 9 0 000-18zm0 3a6 6 0 110 12 6 6 0 010-12z"/></svg>BREAKFAST DAILY</div>
    <div class="perk" style="left:43px;top:348px"><svg viewBox="0 0 26 26"><circle cx="7" cy="5" r="2.5"/><circle cx="19" cy="5" r="2.5"/><path d="M4 9h6v8H9v7H5v-7H4zm12 0h6v8h-1v7h-4v-7h-1z"/></svg>MEET &amp; GREET, WITH<br>BILINGUAL HOSTS</div>

    <div class="perk" style="left:290px;top:246px"><svg viewBox="0 0 26 26"><path d="M2 2h9v7H7l-3 3V9H2zm13 0h9v7h-2v3l-3-3h-4z"/><circle cx="13" cy="15" r="3"/><path d="M8 25c0-4 2-6 5-6s5 2 5 6z"/></svg>Bilingual Local<br>Guides</div>
    <div class="perk" style="left:290px;top:286px"><svg viewBox="0 0 26 26"><path d="M2 15l3-6h16l3 6v5h-3a2 2 0 01-4 0H9a2 2 0 01-4 0H2z"/></svg>Transport</div>
    <div class="perk" style="left:290px;top:320px"><svg viewBox="0 0 26 26"><path d="M3 8h14c4 0 7 3 7 7v3H3zm2 2v3h4v-3zm6 0v3h4v-3zM3 21h21v2H3z"/></svg>Bullet Train</div>
    <div class="perk" style="left:290px;top:354px"><svg viewBox="0 0 26 26"><path d="M6 2h12v22H6zm2 3v12h8V5zm4 14a1.5 1.5 0 100 3 1.5 1.5 0 000-3z"/></svg>Sightseeing</div>

    <svg class="deco" style="left:0;top:380px" width="535" height="120" aria-hidden="true">
      <polygon points="468,10 486,10 456,50 438,50" fill="#666"/>
      <polygon points="490,10 508,10 478,50 460,50" fill="#999"/>
      <polygon points="300,100 360,20 420,20 360,100" fill="var(--red)" opacity=".35"/>
      <polygon points="380,100 450,10 535,10 535,40 480,100" fill="var(--red)" opacity=".75"/>
    </svg>
    <div class="photo luggage-photo" role="img" aria-label="Photo of colourful suitcases stacked on luggage trolleys"></div>
  </div>
</section>

</body>
</html>
```